Corporate Template

Looking for a set of corporate slides to be made which contain multiple different slides and orientations. Looking for at least 8 to 10 different master pages plus a Coversheet and closeout page. Incorporating a color palate similar to our logo coloring is preferred.

I have attached a logo.

```html
<!DOCTYPE html>
<html lang="en">
<head>
<meta charset="utf-8">
<title>Corporate Template – Cover Slide</title>
<link href="https://fonts.googleapis.com/css2?family=Oswald:wght@500;600&family=Lato:wght@400&display=swap" rel="stylesheet">
<style>
  :root {
    --sky-top: #c9d3d6;
    --sky-mid: #aebdbf;
    --hill: #6f8a55;
    --grass: #6d6a4a;
    --ground: #4f4a36;
    --teal: #35b8c4;
    --brand-blue: #2d6fae;
    --white: #ffffff;
    --text-light: #f1f4f4;
    --line: rgba(255,255,255,0.55);
  }
  * { margin: 0; padding: 0; box-sizing: border-box; }
  html, body {
    width: 1200px;
    height: 800px;
    overflow: hidden;
    background: #1d1f20;
  }
  .slide {
    position: relative;
    width: 1200px;
    height: 800px;
    overflow: hidden;
    font-family: "Lato", sans-serif;
  }
  .slide__photo {
    position: absolute;
    inset: 0;
    background:
      linear-gradient(180deg, rgba(0,0,0,0) 60%, rgba(30,28,20,0.35) 100%),
      linear-gradient(180deg,
        var(--sky-top) 0%,
        var(--sky-mid) 38%,
        #9fb19a 48%,
        var(--hill) 58%,
        var(--grass) 76%,
        var(--ground) 100%);
  }
  .brand {
    position: absolute;
    top: 160px;
    left: 0;
    width: 100%;
    display: flex;
    justify-content: center;
    align-items: center;
    gap: 14px;
  }
  .brand__mark {
    width: 34px;
    height: 34px;
    background: var(--brand-blue);
  }
  .brand__name {
    font-family: "Oswald", sans-serif;
    font-weight: 600;
    font-size: 44px;
    letter-spacing: 1px;
    color: var(--brand-blue);
    line-height: 1;
  }
  .headline {
    position: absolute;
    top: 305px;
    left: 0;
    width: 100%;
    text-align: center;
    font-family: "Oswald", sans-serif;
    font-weight: 600;
    text-transform: uppercase;
    line-height: 1.05;
  }
  .headline__lead {
    display: block;
    font-size: 76px;
    color: var(--white);
    padding-left: 20px;
  }
  .headline__main {
    display: block;
    font-size: 92px;
    color: var(--teal);
    margin-left: -60px;
  }
  .points {
    position: absolute;
    top: 628px;
    left: 0;
    width: 100%;
    height: 90px;
  }
  .points__rule {
    position: absolute;
    top: 18px;
    left: 130px;
    width: 980px;
    height: 1px;
    background: var(--line);
  }
  .point {
    position: absolute;
    display: flex;
    align-items: flex-start;
    gap: 14px;
    width: 300px;
  }
  .point--one { left: 118px; top: 0; }
  .point--two { left: 412px; top: 40px; }
  .point--three { left: 728px; top: 55px; }
  .point__num {
    flex: none;
    width: 34px;
    height: 34px;
    border-radius: 50%;
    background: var(--teal);
    color: var(--white);
    font-size: 15px;
    display: flex;
    align-items: center;
    justify-content: center;
  }
  .point__text {
    font-size: 15px;
    line-height: 1.45;
    color: var(--text-light);
    padding-top: 2px;
  }
</style>
</head>
<body>
  <main class="slide">
    <div class="slide__photo" role="img" aria-label="Cover photograph: a businessman relaxing on a chair with his feet on a desk and laptop, set in an open field of green rolling hills under a pale cloudy sky"></div>

    <div class="brand">
      <span class="brand__mark"></span>
      <span class="brand__name">HALVERN CO</span>
    </div>

    <h1 class="headline">
      <span class="headline__lead">Just Starting</span>
      <span class="headline__main">The Presentation</span>
    </h1>

    <section class="points">
      <div class="points__rule"></div>
      <div class="point point--one">
        <span class="point__num">1</span>
        <p class="point__text">Lorem Ipsum is simply dummy text of the printing and typesetting industry.</p>
      </div>
      <div class="point point--two">
        <span class="point__num">2</span>
        <p class="point__text">Lorem Ipsum is simply dummy text of the printing and typesetting industry.</p>
      </div>
      <div class="point point--three">
        <span class="point__num">3</span>
        <p class="point__text">Lorem Ipsum is simply dummy text of the printing and typesetting industry.</p>
      </div>
    </section>
  </main>
</body>
</html>
```